Brixom Vale needs a powerpoint design

We need a powerpoint design for an Information Technology based in Fairfax call "Brixom Vale". We are Information Technology solutions provider for the Federal Government. We develop Talvex, Mobile and Cloud based solutions. We support the Healthcare and Financial sectors of the Government. We would like to see designs that use the colors of our logo. We've attached a copy of our logo. The final design should communicate Information Technology and System Integration with Agile Development.

Target Market(s)

Our target market is the Federal Government and System Integators in the Washington DC area.

Industry/Entity Type

Government

Requirements
Must have
• The powerpoint design must have a professional look.

```html
<!DOCTYPE html>
<html lang="en">
<head>
<meta charset="utf-8">
<title>Brixom Vale – Presentation Template</title>
<link href="https://fonts.googleapis.com/css2?family=Open+Sans:wght@400;600;700;800&display=swap" rel="stylesheet">
<style>
  :root {
    --page-bg: #e9edf2;
    --slide-white: #ffffff;
    --grey-light: #f4f4f4;
    --grey-mid: #c9c9c9;
    --blue-deep: #0c4f9c;
    --blue-mid: #1c6bbd;
    --blue-light: #3d8fd6;
    --brand-navy: #1f3f8f;
    --accent-green: #9bd03b;
    --ink: #111111;
    --ink-soft: #333333;
    --rule-blue: #2a7fcb;
    --photo-dark: #1c2633;
    --photo-warm: #6f5a45;
  }
  * { box-sizing: border-box; margin: 0; padding: 0; }
  html, body {
    width: 1056px; height: 1200px; overflow: hidden;
    background: var(--page-bg);
    font-family: "Open Sans", Arial, sans-serif;
  }
  .slide {
    position: absolute; left: 188px; width: 680px; height: 510px;
    background: var(--slide-white);
    box-shadow: 0 2px 10px rgba(0,0,0,0.18);
    overflow: hidden;
  }
  .slide--title { top: 50px;
    background: linear-gradient(180deg, #c4c4c4 0%, #f2f2f2 14%, #e9e9e9 22%, #e6e6e6 78%, #c9c9c9 90%, #f4f4f4 100%);
  }
  .slide--content { top: 640px; }

  /* wordmark */
  .wordmark {
    display: flex; align-items: center; gap: 8px;
    color: var(--brand-navy); font-weight: 700; letter-spacing: 0.2px;
  }
  .wordmark__square { width: 18px; height: 18px; background: var(--brand-navy); }

  /* title slide */
  .title-slide__brand { position: absolute; top: 52px; left: 0; right: 0; justify-content: center; font-size: 20px; }
  .title-slide__band {
    position: absolute; top: 116px; left: 0; right: 0; height: 274px;
    background: radial-gradient(ellipse at 50% 45%, var(--blue-light) 0%, var(--blue-mid) 45%, var(--blue-deep) 100%);
    box-shadow: 0 8px 14px rgba(0,0,0,0.25);
  }
  .title-slide__heading {
    position: absolute; top: 115px; left: 0; right: 0; text-align: center;
    color: #fff; font-size: 36px; font-weight: 600; letter-spacing: 0.5px;
  }
  .title-slide__sub {
    position: absolute; top: 165px; left: 0; right: 0; text-align: center;
    color: var(--accent-green); font-size: 14px; font-weight: 700; letter-spacing: 0.4px;
  }
  .title-slide__url {
    position: absolute; top: 430px; left: 0; right: 0; text-align: center;
    color: var(--ink-soft); font-size: 11px;
  }
  .title-slide__copy {
    position: absolute; top: 457px; left: 0; right: 0; text-align: center;
    color: var(--blue-mid); font-size: 10.5px;
  }

  /* content slide */
  .content-slide__heading {
    position: absolute; top: 40px; left: 40px;
    font-size: 18px; font-weight: 700; color: var(--ink); letter-spacing: 0.3px;
  }
  .content-slide__rule { position: absolute; top: 72px; left: 0; right: 0; height: 3px; background: var(--rule-blue); }
  .content-slide__photo {
    position: absolute; top: 135px; left: 80px; width: 230px; height: 280px;
    background: linear-gradient(165deg, var(--photo-dark) 0%, #2e4660 45%, var(--photo-warm) 85%, #8a4b3a 100%);
  }
  .content-slide__body {
    position: absolute; top: 135px; left: 340px; width: 247px;
    font-size: 10.4px; line-height: 1.5; color: var(--ink); text-align: justify;
  }
  .content-slide__body p + p { margin-top: 13px; }
  .content-slide__footer {
    position: absolute; top: 480px; left: 0; width: 490px; height: 13px;
    background: var(--brand-navy); color: #fff; font-size: 8px; line-height: 13px;
  }
  .footer__num { position: absolute; left: 42px; }
  .footer__url { position: absolute; left: 72px; }
  .footer__date { position: absolute; left: 430px; }
  .content-slide__brand { position: absolute; top: 477px; left: 502px; font-size: 17px; }
</style>
</head>
<body>

<section class="slide slide--title">
  <div class="wordmark title-slide__brand"><span class="wordmark__square"></span>Brixom Vale</div>
  <div class="title-slide__band">
    <h1 class="title-slide__heading">PRESENTATION TITTLE HERE</h1>
    <p class="title-slide__sub">YOUR PRESENTATION&nbsp; SUB TITLE HERE</p>
  </div>
  <p class="title-slide__url">www.brixomvale.com</p>
  <p class="title-slide__copy">© 2013 Brixom Vale. All rights reserved.</p>
</section>

<section class="slide slide--content">
  <h2 class="content-slide__heading">BRIXOM VALE PRESENTATION POWERFUL MISSION 1</h2>
  <div class="content-slide__rule"></div>
  <div class="content-slide__photo" role="img" aria-label="Photo of a lit glass office tower at dusk"></div>
  <div class="content-slide__body">
    <p>The NRCF has forged a courageous and dynamic approach to the methodology of cancer research. By overcoming previous pitfalls that held the industry back, the NRCF has propelled the frontier of multiple myeloma research to a new level.</p>
    <p>Essential to this approach are 4 revious pitfalls that held the industry back, the NRCF has propelled the frontier of multiple myeloma research to a new level. groundbreaking initiatives that have revolutionized the way research and drug development are conducted. With these models, the NRCF can dramatically accelerate.</p>
    <p>Groundbreaking initiatives that have revolutionized the way research and drug development are conducted.</p>
  </div>
  <div class="content-slide__footer">
    <span class="footer__num">1</span>
    <span class="footer__url">www.brixomvale.com</span>
    <span class="footer__date">27/12/2013</span>
  </div>
  <div class="wordmark content-slide__brand"><span class="wordmark__square"></span>Brixom Vale</div>
</section>

</body>
</html>
```